inspirational business card

I want to use the Vector on Pixavend.com (number 58172046) and I will purchase the vector to send it to the designer once the general concept is approved. You can download it for free for a one time use on providing a design for this request.
Within the vector, insert:
Tessa Brundle
Guidance and Partnering

I prefer a vertical card but do not require vertical.

Contact info:

Tessa Brundle, J.D.
Collaborative Lawyer
Certified Divorce Coach
Mediation Coach
PHONE 515/555-0143
EMAIL: tbjd@quellmail.net

Website: Guidanceandpartnering.com
Settlementcourse.com

I like greens, blue and grey. I do not want black font, and would like the font to be legible without needing perfect reading vision (no super small font).
I would like the overall theme to convey growth and nurturance.
I like the vector I selected because of the growth and light portrayed.
Not too frilly or too bold. I would like to to appeal to both sexes.

Target Market(s)

Generally professional women 35-60

Industry/Entity Type

Attorney

Font styles to use
Serif
Sans Serif

Colors
acd136
cadf82
fbf289
9d9d9d

Requirements
Must have
• My project does not need to have my photo but you could use it if you want
Nice to have
• Vertical
• I like rounded edges on the cards
Should not have
• I do not like my name appearing two times in close proximity. I'm not a flowery person.

```html
<!DOCTYPE html>
<html lang="en">
<head>
<meta charset="utf-8">
<title>Tessa Brundle, J.D. – Business Card</title>
<link href="https://fonts.googleapis.com/css2?family=Roboto:wght@300;400&display=swap" rel="stylesheet">
<style>
  :root {
    --canvas-grey: #e6e7e9;
    --card-blue: #0eacd0;
    --band-blue: #5dbcd8;
    --card-white: #ffffff;
    --tree-light: #6fcbe3;
    --mark-grey: #555a60;
  }
  html, body {
    margin: 0;
    padding: 0;
    overflow: hidden;
  }
  body {
    width: 1200px;
    height: 663px;
    background: var(--canvas-grey);
    position: relative;
    font-family: "Roboto", Arial, sans-serif;
  }
  .crop-marks {
    position: absolute;
    left: 0;
    top: 0;
  }
  .card {
    position: absolute;
    left: 56px;
    width: 474px;
    height: 295px;
    border-radius: 19px;
    overflow: hidden;
  }
  .card--front { top: 38px; background: var(--card-white); }
  .card--back  { top: 343px; background: var(--card-blue); }
  .card__shape {
    position: absolute;
    inset: 0;
  }
  .identity {
    position: absolute;
    right: 17px;
    top: 52px;
    text-align: right;
    color: var(--card-white);
    font-weight: 300;
  }
  .identity__name {
    margin: 0;
    font-size: 24px;
    font-weight: 400;
    line-height: 1.1;
  }
  .identity__role {
    margin: 0;
    font-size: 12.5px;
    line-height: 15px;
  }
  .contact-list {
    position: absolute;
    left: 243px;
    top: 137px;
    margin: 0;
    padding: 0;
    list-style: none;
    color: var(--card-white);
    font-size: 12.5px;
    font-weight: 300;
  }
  .contact-list__item {
    display: flex;
    align-items: flex-start;
    gap: 11px;
    margin-bottom: 10px;
  }
  .contact-list__icon {
    flex: none;
    width: 26px;
    height: 26px;
  }
  .contact-list__text {
    line-height: 15px;
    padding-top: 5px;
  }
  .tree-art {
    position: absolute;
    border-radius: 50%;
  }
  .tree-art--front {
    left: 30px;
    top: 65px;
    width: 148px;
    height: 148px;
    background: radial-gradient(circle at 50% 40%, var(--tree-light), var(--card-blue));
  }
  .tree-art--back {
    left: 129px;
    top: 23px;
    width: 198px;
    height: 198px;
    background: radial-gradient(circle at 50% 40%, #ffffff, #bfe9f4);
  }
  .brand {
    position: absolute;
    left: 0;
    right: 0;
    top: 228px;
    text-align: center;
    color: var(--card-white);
    font-weight: 400;
  }
  .brand__name {
    margin: 0;
    font-size: 15px;
    line-height: 18px;
  }
  .brand__tagline {
    margin: 2px 0 0;
    font-size: 10px;
  }
</style>
</head>
<body>

<svg class="crop-marks" width="1200" height="663" viewBox="0 0 1200 663" aria-hidden="true">
  <g stroke="var(--mark-grey)" stroke-width="1">
    <line x1="14" y1="36" x2="19" y2="36"/><line x1="22" y1="28" x2="22" y2="33"/>
    <line x1="481" y1="36" x2="486" y2="36"/><line x1="476" y1="27" x2="476" y2="32"/>
    <line x1="14" y1="308" x2="19" y2="308"/><line x1="22" y1="314" x2="22" y2="319"/>
    <line x1="481" y1="308" x2="486" y2="308"/><line x1="476" y1="314" x2="476" y2="319"/>
    <line x1="14" y1="350" x2="19" y2="350"/><line x1="22" y1="342" x2="22" y2="347"/>
    <line x1="481" y1="350" x2="486" y2="350"/><line x1="476" y1="341" x2="476" y2="346"/>
    <line x1="14" y1="623" x2="19" y2="623"/><line x1="22" y1="629" x2="22" y2="634"/>
    <line x1="481" y1="623" x2="486" y2="623"/><line x1="476" y1="629" x2="476" y2="634"/>
  </g>
</svg>

<section class="card card--front" aria-label="Card front">
  <svg class="card__shape" width="474" height="295" viewBox="0 0 474 295" aria-hidden="true">
    <path d="M228 0 C 196 90, 190 190, 233 295 L474 295 L474 0 Z" fill="var(--band-blue)"/>
    <path d="M246 0 C 212 90, 206 190, 250 295 L474 295 L474 0 Z" fill="var(--card-blue)"/>
  </svg>

  <div class="tree-art tree-art--front" role="img" aria-label="Tree of life illustration in a crescent circle"></div>

  <div class="identity">
    <h1 class="identity__name">Tessa Brundle, J.D.</h1>
    <p class="identity__role">Collaborative Lawyer</p>
    <p class="identity__role">Certified Divorce Coach</p>
    <p class="identity__role">Mediation Coach</p>
  </div>

  <ul class="contact-list">
    <li class="contact-list__item">
      <svg class="contact-list__icon" viewBox="0 0 26 26" aria-hidden="true">
        <circle cx="13" cy="13" r="12" fill="none" stroke="#fff" stroke-width="1.4"/>
        <path d="M9.5 7.5 l2 -0.5 l1.3 3 l-1.5 1.2 c0.7 1.6 1.8 2.7 3.4 3.4 l1.2 -1.5 l3 1.3 l-0.5 2 c-5 0.4 -9.3 -3.9 -8.9 -8.9z" fill="#fff"/>
      </svg>
      <span class="contact-list__text">515/555-0143</span>
    </li>
    <li class="contact-list__item">
      <svg class="contact-list__icon" viewBox="0 0 26 26" aria-hidden="true">
        <circle cx="13" cy="13" r="12" fill="none" stroke="#fff" stroke-width="1.4"/>
        <rect x="7" y="9" width="12" height="8.5" fill="none" stroke="#fff" stroke-width="1.3"/>
        <path d="M7 9 l6 5 l6 -5" fill="none" stroke="#fff" stroke-width="1.3"/>
      </svg>
      <span class="contact-list__text">tbjd@quellmail.net</span>
    </li>
    <li class="contact-list__item">
      <svg class="contact-list__icon" viewBox="0 0 26 26" aria-hidden="true">
        <circle cx="13" cy="13" r="12.5" fill="#fff"/>
        <text x="13" y="15.5" text-anchor="middle" font-size="6.5" font-family="Roboto, Arial, sans-serif" fill="var(--card-blue)">www</text>
      </svg>
      <span class="contact-list__text">guidanceandpartnering.com<br>settlementcourse.com</span>
    </li>
  </ul>
</section>

<section class="card card--back" aria-label="Card back">
  <div class="tree-art tree-art--back" role="img" aria-label="Tree of life illustration in a white crescent circle"></div>
  <div class="brand">
    <p class="brand__name">Tessa Brundle</p>
    <p class="brand__tagline">Guidance and Partnering</p>
  </div>
</section>

</body>
</html>
```